Design a great website for our amazing new country club in Southern California!

Our old neighborhood golf club is being transformed into a 100% new world-class club located down the street from the old location. We want a new website look that projects our new image. However because the club hasn't been built yet, we don't have a lot of images--just a new logo and a few renderings. So we will add images in the coming months as things get built. In the meantime, for things such as restaurant or swimming or tennis pics, feel free to plug in stock internet images for now. And regarding the movie file, we had an idea for a dramatic headline slowly rising over the clubhouse. It's just an idea, however, we're not married to it. We need to get creative here, as we have so few images. Oh, and we definitely want one main graphic on the home page. We don't like the slide-show effect--looks cheap. And finally, the landing page will be a 'public' page with other pages aimed at attracting new members. There will also be a 'Members area' that is password-protected. Site maps and rough copy for each of the two sections is included. Good luck!! :-) Please view our current website: sagemeadowcc.com

Wealthy folks who like golf, sports and dining. Our memberships range in price from $18,000 to $130,000.

Club

Coded - Design and coding required

5+ page

Sans Serif

• a GORGEOUS home page, with buttons and features that will remain static on all other pages. We want the navigation buttons along the top with pull-downs. Only the areas below the nav buttons will change. We want this site to look very clean and classy.
• Maybe have the button 'glow' or enlarge or whatever when you roll over them. Whatever can spruce up the simple classy design. Maybe so some special effect to the SM logo as well. As long as it looks classy, that's the main thing. And if you can find some good generic images of golf, dining, swimming, tennis, whatever on the net, feel free to use them.
• No slide show effects, with multiple images changing.

```html
<!DOCTYPE html>
<html lang="en">
<head>
<meta charset="utf-8">
<title>Sage Meadow Country Club</title>
<link href="https://fonts.googleapis.com/css2?family=Open+Sans:ital,wght@0,400;0,600;0,700;1,700;1,800&display=swap" rel="stylesheet">
<style>
:root{
  --green-deep:#0b2e14;
  --green:#0f4a1e;
  --green-mid:#2f7a2a;
  --gold:#f2c500;
  --cream:#fdf3c6;
  --ink:#1f2a1f;
  --navy:#0f1f33;
  --navy-dark:#091524;
  --panel:#1b2b3d;
  --white:#ffffff;
  --muted:#9fb0c2;
}
*{margin:0;padding:0;box-sizing:border-box}
html,body{width:1200px;height:2280px;overflow:hidden}
body{font-family:"Open Sans",sans-serif;color:var(--ink);position:relative;background:var(--white)}
.block{position:absolute;left:0;width:1200px}

/* header */
.site-header{top:0;height:136px;background:linear-gradient(var(--green-deep),var(--green));display:flex;align-items:center;justify-content:center}
.brand{display:flex;align-items:center;gap:14px;color:var(--gold);font-weight:700;font-size:22px;letter-spacing:3px}
.brand-dot{width:54px;height:54px;border-radius:50%;background:var(--gold)}
.main-nav{top:136px;height:36px;background:var(--green-deep);display:flex;justify-content:center;align-items:center;gap:4px}
.main-nav a{color:var(--white);font-size:11px;font-weight:600;text-decoration:none;padding:8px 16px;letter-spacing:.5px}
.main-nav a.members{background:var(--gold);color:var(--green-deep);margin-left:14px}

/* hero */
.hero{top:172px;height:388px;background:linear-gradient(180deg,#a9c9e6 0%,#d8e7ef 30%,#7fae4a 52%,#3f7d22 100%)}
.hero-copy{position:absolute;left:60px;top:150px;width:560px;color:var(--white)}
.hero-copy h1{font-style:italic;font-weight:800;font-size:42px;text-shadow:0 2px 6px rgba(0,0,0,.4)}
.hero-copy p{font-size:13px;line-height:1.6;margin:10px 0 18px}
.btn-outline{display:inline-block;border:1px solid currentColor;font-size:10px;font-weight:600;padding:7px 16px;letter-spacing:1px;color:inherit}

/* about */
.about{top:560px;height:368px;background:var(--cream)}
.about-copy{position:absolute;left:60px;top:40px;width:500px}
.about-copy h2{font-size:30px;font-weight:700;color:var(--green)}
.est{display:flex;align-items:center;gap:10px;font-style:italic;font-size:13px;font-weight:700;color:var(--green);margin:6px 0 18px}
.est::before,.est::after{content:"";flex:1;height:1px;background:var(--green)}
.est::before{flex:0 0 40px}
.about-copy p{font-size:12px;line-height:1.7;margin-bottom:12px}
.about-copy .btn-outline{color:var(--green)}
.rendering{position:absolute;left:600px;top:20px;width:590px;height:330px;background:linear-gradient(135deg,#e9eee0,#c9d8b4 50%,#9fbf86)}

/* features */
.features{top:928px;height:392px;background:linear-gradient(180deg,#8fb6c9,#5b8d9a 45%,#3e5d49)}
.section-title{font-style:italic;font-weight:800;font-size:34px}
.features .section-title{position:absolute;left:60px;top:26px;color:var(--gold)}
.features .sub{position:absolute;left:62px;top:72px;font-size:12px;color:var(--white);font-style:italic}
.cards{position:absolute;left:150px;top:110px;display:flex;gap:0;width:900px}
.card{width:225px;height:260px;background:var(--white);border-right:1px solid #ddd;display:flex;flex-direction:column;align-items:center;padding-top:30px;text-align:center}
.card svg{width:56px;height:56px;stroke:#777;fill:none;stroke-width:2}
.card h3{font-size:14px;font-weight:600;color:#444;margin-top:18px;line-height:1.4}
.card .more{margin-top:auto;margin-bottom:18px;width:180px;border-top:1px solid #ccc;padding-top:10px;font-size:10px;font-weight:700;color:var(--green);text-align:left}

/* gallery */
.gallery{top:1320px;height:320px;background:var(--green)}
.gallery .section-title{position:absolute;left:60px;top:14px;color:var(--white)}
.gallery .btn-outline{position:absolute;right:60px;top:28px;color:var(--white)}
.grid{position:absolute;top:70px;left:0;display:grid;grid-template-columns:repeat(8,150px);grid-auto-rows:125px}
.g1{background:linear-gradient(#9cc6e6,#5c9a38)}
.g2{background:linear-gradient(#c9e0ef,#3f7f22)}
.g3{background:linear-gradient(#e7d9a3,#6a9b32)}
.g4{background:linear-gradient(#8fb7d6,#2e6b1e)}
.g5{background:linear-gradient(#f0a23a,#4d6f1f)}
.g6{background:linear-gradient(#f6c25a,#3e6a1a)}

/* map + contact */
.map{top:1640px;height:360px;background:linear-gradient(135deg,#e6ebef,#cfd9e2 50%,#8fb3cf)}
.contact{position:absolute;right:140px;top:20px;width:190px;height:320px;background:var(--panel);padding:20px 16px;color:var(--white)}
.contact h2{font-size:20px;font-weight:600}
.contact p{font-size:9px;color:var(--muted);margin:4px 0 14px;line-height:1.5}
.field{height:24px;background:var(--white);margin-bottom:10px}
.field.msg{height:56px}
.submit{display:inline-block;border:1px solid var(--white);font-size:9px;padding:6px 12px;letter-spacing:1px}

/* footer */
.site-footer{top:2000px;height:240px;background:var(--navy);color:var(--muted);display:flex;gap:0;padding:40px 0 0 150px}
.col{width:230px;font-size:10px;line-height:2}
.col h4{color:var(--white);font-size:10px;font-weight:700;letter-spacing:1px;margin-bottom:8px}
.socials{display:flex;gap:6px;margin-bottom:14px}
.socials span{width:22px;height:22px;border-radius:50%;background:var(--gold)}
.badge{width:150px;height:44px;background:var(--white);border-radius:4px}
.copyright{top:2240px;height:40px;background:var(--navy-dark);color:var(--muted);font-size:9px;text-align:center;line-height:40px}
</style>
</head>
<body>

<header class="block site-header">
  <div class="brand"><span class="brand-dot"></span>SAGE MEADOW</div>
</header>

<nav class="block main-nav">
  <a>HOME</a><a>ABOUT US</a><a>CLUB NEWS</a><a>GOLF CLUBS</a><a>MEMBERSHIP</a><a>WEDDINGS &amp; EVENTS</a><a class="members">MEMBERS CLUB</a>
</nav>

<section class="block hero" role="img" aria-label="Golf ball on a tee over a green fairway">
  <div class="hero-copy">
    <h1>Lorel Ipsum Dolor Sit Amet</h1>
    <p>Sed ut perspiciatis unde omnis iste natus error sit voluptatem accusantium doloremque laudantium, totam rem aperiam, eaque ipsa quae ab illo inventore.</p>
    <span class="btn-outline">READ MORE</span>
  </div>
</section>

<section class="block about">
  <div class="about-copy">
    <h2>Sage Meadow Country Club</h2>
    <div class="est">Established 1965</div>
    <p>Nor again is there anyone who loves or pursues or desires to obtain pain of itself, because it is pain, but occasionally circumstances occur in which toil and pain can procure him some great pleasure. To take a trivial example, which of us ever undertakes laborious exercise.</p>
    <p>But who has any right to find fault with a man who chooses to enjoy a pleasure that has no annoying consequences, or one who avoids a pain that produces no resultant pleasure at all.</p>
    <span class="btn-outline">READ MORE</span>
  </div>
  <div class="rendering" role="img" aria-label="Aerial rendering of the new clubhouse and grounds"></div>
</section>

<section class="block features" role="img" aria-label="Resort pool terrace at dusk">
  <h2 class="section-title">Special Features</h2>
  <div class="sub">Lorem ipsum dolor</div>
  <div class="cards">
    <div class="card">
      <svg viewBox="0 0 56 56"><path d="M20 50V6l20 8-20 8"/><ellipse cx="20" cy="50" rx="14" ry="3"/></svg>
      <h3>GOLF &amp;<br>RESTAURANT<br>PACKAGES</h3><div class="more">READ MORE »</div>
    </div>
    <div class="card">
      <svg viewBox="0 0 56 56"><circle cx="21" cy="32" r="13"/><circle cx="35" cy="32" r="13"/><path d="M24 12l4-6 4 6z"/></svg>
      <h3>WEDDING<br>&amp; OTHER<br>EVENTS</h3><div class="more">READ MORE »</div>
    </div>
    <div class="card">
      <svg viewBox="0 0 56 56"><rect x="14" y="6" width="28" height="44" rx="2"/><path d="M20 16h16M20 24h16M20 32h16M20 40h10"/></svg>
      <h3>SPECIAL<br>RESTAURANT<br>MENU</h3><div class="more">READ MORE »</div>
    </div>
    <div class="card">
      <svg viewBox="0 0 56 56"><circle cx="34" cy="12" r="5"/><path d="M12 30l12-10 10 8"/><path d="M4 42q6-5 12 0t12 0 12 0 12 0M4 50q6-5 12 0t12 0 12 0 12 0"/></svg>
      <h3>SWIMMING<br>AND OTHER<br>SPORTS</h3><div class="more">READ MORE »</div>
    </div>
  </div>
</section>

<section class="block gallery">
  <h2 class="section-title">Our Gallery</h2>
  <span class="btn-outline">VIEW MORE</span>
  <div class="grid" role="img" aria-label="Grid of golf course photographs">
    <div class="g1"></div><div class="g2"></div><div class="g3"></div><div class="g4"></div><div class="g2"></div><div class="g1"></div><div class="g4"></div><div class="g3"></div>
    <div class="g5"></div><div class="g2"></div><div class="g6"></div><div class="g4"></div><div class="g1"></div><div class="g3"></div><div class="g6"></div><div class="g2"></div>
  </div>
</section>

<section class="block map" role="img" aria-label="Street map showing the club location">
  <div class="contact">
    <h2>Contact Us</h2>
    <p>Send us a note and our team will reply shortly.</p>
    <div class="field"></div><div class="field"></div><div class="field msg"></div>
    <span class="submit">SUBMIT</span>
  </div>
</section>

<footer class="block site-footer">
  <div class="col"><h4>QUICK LINKS</h4>Home<br>About Us<br>Club News<br>Golf Clubs<br>Membership<br>Weddings &amp; Events<br>Members Club</div>
  <div class="col"><h4>LATEST NEWS</h4>New clubhouse design unveiled<br>Spring tee times now open<br>Pool terrace opens this summer<br>Dining menu preview</div>
  <div class="col"><h4>CONTACT US</h4>1450 Meadow Crest Drive<br>Sage Valley, CA 92000<br>Phone: (555) 014-2290<br>info@sagemeadowcc.com<br>sagemeadowcc.com</div>
  <div class="col"><h4>CONNECT WITH US</h4><div class="socials"><span></span><span></span><span></span><span></span><span></span></div><div class="badge"></div></div>
</footer>

<div class="block copyright">Copyright © 2024 Sage Meadow Country Club. All rights reserved.</div>

</body>
</html>
```